Landing Page for an INNOVATIVE Quilt Cover, with "how it works" section

Before I describe what I would like, you need to understand these:

1) This is a marketing page. The PRIMARY OBJECTIVE is to collect email addresses.
2) The target audience is 35 year old stay-at-home mums. Appeal to them (so don't throw in gadgets in your design!)
3) Make the design as SIMPLE and CLEAR as you can.

Alright, let's begin!

I've created a company called "Quollin", and a product called "Snug-Fit Wrap". Quollin is just a name, but the product is what I NEED to visually explain to the target audience.

Very very briefly, the Snug-Fit Wrap opens on 3 sides, and are bound together by velcro. The primary purpose - is to put a smile on the face of a 35 year old mum every time she changes the quilt cover...

In other words, it makes the chore of changing the cover PAINLESS.

The Snug-Fit Wrap also has strategically placed velcro pieces on the underside (refer attached picture). These velcro pieces hold the quilt in place once it's in the cover. You know how sometimes you have a ball of quilt trapped at the bottom of your cover after using it for a couple of weeks? This gets rid of that problem.

So now on to the design...

1) This needs to be a simple, one-page design (in case it's not clear enough!)

2) As I said, the primary objective of this site is to collect email addresses. Therefore, please incorporate a 'form' within your design.

I only need email addresses (i.e. no need for a separate box for names, country etc) but please allow for social plugins (Facebook, Twitter and Email).

These are some sites you can get inspiration from in terms of the general layout (and simplicity) I want:
- http://brimfolio.com/
- http://www.parvonix.com/
- http://www.ambertwigkit.com/
- http://vintrel.ws/

3) I need you to design a "How It Works" section, which CLEARLY describes how the Snug-Fit Wrap works.

This is my current site: www.quollin.com, It's an e-commerce store which will be disabled soon, but the homepage should give you a good idea of how the Snug-Fit Wrap works (PLEASE NOTE: I DISLIKE my current design as it's still slightly confusing and boorrrriing).

IMPORTANT - It is not critical to show "what's in the box".

These are some sites which may give you an idea of how to design the "how it works" section:
- http://www.pembrook.com/purse/how-it-works.html
- http://www.lantoloan.com/How-LantoLoan-Works-sp-1.html

4) It's OK to raise their curiosity, but as long as your design explains enough of how the product works.

Make it fun.

Remember, I am after those email addresses.

To all designers working on this project:

Part of this job is to re-design the "how it works" section.  Please DO NOT retain the same design you see on www.quollin.com (or merely re-arrange what I already have on quollin.com).

If you have done that, it is likely you will not be picked.

Thanks, and good luck!

Hi All, 

I have updated a raw vector file of my previous design.  This was one of the earlier drafts, so please feel free to edit it.

PLEASE NOTE - as I indicated in my brief, I'm looking for new ideas for this "how-it-works" section, as I dislike this current design.

Thanks

Target Market(s)

30-40 year old, stay at home mums.

Industry/Entity Type

E-Commerce

Requirements
Must have
• - Name of company and product i.e. Quollin Snug-Fit Wrap
- A tagline under the company name and product. For now, go with "Never Struggle To Change Your Quilt Cover Again"

- Have this other tagline somewhere (this is optional):
"We will change the way you use your quilt cover...forever"
Should not have
• nothing is prohibited. Go crazy!

```html
<!DOCTYPE html>
<html lang="en">
<head>
<meta charset="utf-8">
<title>Quollin Snug-Fit Wrap</title>
<link href="https://fonts.googleapis.com/css2?family=PT+Sans:wght@400;700&display=swap" rel="stylesheet">
<style>
  :root {
    --bg-top: #8fd6d2;
    --bg-mid: #c6ecea;
    --bg-low: #f3fbfb;
    --band: #7ccbc6;
    --band-foot: #b3e1de;
    --teal-dark: #13584f;
    --teal: #1b7a70;
    --orange: #d9560f;
    --orange-light: #f38a35;
    --text: #333a3a;
    --form-box: #7fcac5;
    --arrow: #9aa5a5;
    --step1: #e8e4b0;
    --step2: #f0cf9b;
    --step3: #dccdf0;
    --step4: #f5c6bd;
    --step5: #a9e2e0;
    --sketch: #f4f4f2;
  }
  * { box-sizing: border-box; margin: 0; padding: 0; }
  html, body { width: 1200px; height: 1200px; overflow: hidden; }
  body {
    position: relative;
    font-family: "PT Sans", sans-serif;
    color: var(--text);
    background: radial-gradient(ellipse 560px 420px at 600px 560px, #ffffff 0%, rgba(255,255,255,0) 70%),
                linear-gradient(180deg, var(--bg-top) 0%, var(--bg-mid) 35%, var(--bg-low) 80%, #ffffff 100%);
  }
  .top-bar {
    position: absolute; left: 0; top: 0; width: 1200px; height: 36px;
    background: var(--band);
  }
  .top-nav {
    position: absolute; right: 186px; top: 11px;
    font-size: 11.5px; color: #1d2b2b; text-transform: uppercase;
    display: flex; gap: 12px;
  }
  .brand {
    position: absolute; left: 0; top: 62px; width: 1212px; text-align: center;
    font-size: 42px; font-weight: 700; color: var(--teal); letter-spacing: -0.5px;
  }
  .tagline {
    position: absolute; left: 0; top: 150px; width: 1210px; text-align: center;
    font-size: 19px; color: var(--teal-dark);
  }
  .signup {
    position: absolute; left: 328px; top: 181px; width: 572px; height: 66px;
    background: var(--form-box); border-radius: 8px;
  }
  .signup-input {
    position: absolute; left: 15px; top: 13px; width: 405px; height: 40px;
    background: #fff; border: none; font: 13.5px "PT Sans", sans-serif; color: #555;
    padding: 11px 14px;
  }
  .signup-button {
    position: absolute; left: 426px; top: 13px; width: 126px; height: 40px;
    background: linear-gradient(180deg, var(--orange-light), var(--orange));
    border: 1px solid #c14a0a; color: #fff; font: 700 20px "PT Sans", sans-serif;
  }
  .spam-note {
    position: absolute; left: 688px; top: 254px; font-size: 12px; color: #333;
  }
  .spam-note .star { color: var(--orange); margin-right: 6px; }
  .steps { position: absolute; left: 0; top: 0; }
  .step-label {
    position: absolute; font-size: 17px; font-weight: 700; color: #3b3b3b;
    text-align: center; line-height: 19px; letter-spacing: -0.3px;
  }
  .how-title {
    position: absolute; left: 460px; top: 570px; width: 300px; text-align: center;
    font-size: 30px; font-weight: 700; color: var(--teal-dark);
  }
  .divider {
    position: absolute; left: 168px; top: 917px; width: 870px; height: 1px; background: #cfd8d8;
  }
  .pitch { position: absolute; left: 188px; top: 943px; width: 850px; }
  .pitch-question { font-size: 16.5px; font-weight: 700; color: var(--orange); }
  .pitch-answer { margin-top: 12px; font-size: 17px; font-weight: 700; color: var(--teal); }
  .pitch-body { margin-top: 14px; font-size: 11.7px; line-height: 16.6px; color: #333; }
  .pitch-body + .pitch-body { margin-top: 17px; }
  .footer {
    position: absolute; left: 0; top: 1165px; width: 1200px; height: 35px;
    background: var(--band-foot); text-align: center; padding-top: 9px;
    font-size: 11.5px; color: #3d5a58;
  }
</style>
</head>
<body>
  <div class="top-bar">
    <nav class="top-nav"><span>Visit Store</span><span>|</span><span>FAQ</span><span>|</span><span>About Us</span></nav>
  </div>

  <h1 class="brand">Quollin Snug-Fit Wrap</h1>
  <p class="tagline">Never Struggle to Change Your Quilt Cover Again</p>

  <form class="signup">
    <input class="signup-input" type="email" placeholder="Type your email address">
    <button class="signup-button" type="button">Submit</button>
  </form>
  <p class="spam-note"><span class="star">★</span>We hate spams as much as you do.</p>

  <svg class="steps" width="1200" height="920" viewBox="0 0 1200 920">
    <defs>
      <marker id="arrow-head" viewBox="0 0 10 10" refX="6" refY="5" markerWidth="7" markerHeight="7" orient="auto">
        <path d="M1 1 L7 5 L1 9" fill="none" stroke="var(--arrow)" stroke-width="1.4"/>
      </marker>
    </defs>
    <g class="step-discs">
      <circle cx="372" cy="582" r="108" fill="#fff" opacity="0.8"/>
      <circle cx="369" cy="579" r="108" fill="var(--step1)"/>
      <circle cx="566" cy="407" r="108" fill="#fff" opacity="0.8"/>
      <circle cx="563" cy="404" r="108" fill="var(--step2)"/>
      <circle cx="822" cy="469" r="108" fill="#fff" opacity="0.8"/>
      <circle cx="819" cy="466" r="108" fill="var(--step3)"/>
      <circle cx="803" cy="720" r="108" fill="#fff" opacity="0.8"/>
      <circle cx="800" cy="717" r="108" fill="var(--step4)"/>
      <circle cx="536" cy="788" r="108" fill="#fff" opacity="0.8"/>
      <circle cx="533" cy="785" r="108" fill="var(--step5)"/>
    </g>
    <g class="step-illustrations" fill="var(--sketch)" stroke="#c9c9c9">
      <ellipse role="img" aria-label="Quilt with velcro pieces being attached, with a zoomed inset of a hand pressing a velcro tab" cx="345" cy="630" rx="62" ry="36"/>
      <ellipse role="img" aria-label="Quilt being slid into the open cover" cx="575" cy="437" rx="70" ry="40"/>
      <ellipse role="img" aria-label="Cover flap folding over the quilt to fasten it" cx="835" cy="502" rx="80" ry="40"/>
      <ellipse role="img" aria-label="Hands pressing the velcro closed along all sides of the cover" cx="805" cy="755" rx="85" ry="38"/>
      <ellipse role="img" aria-label="Neatly made bed with the finished quilt cover" cx="545" cy="828" rx="72" ry="40"/>
    </g>
    <g class="step-numbers" font-family="PT Sans, sans-serif" font-size="18" text-anchor="middle" fill="#222">
      <circle cx="373" cy="502" r="14" fill="#fff" stroke="#ccc"/><text x="373" y="508">1</text>
      <circle cx="566" cy="329" r="14" fill="#fff" stroke="#ccc"/><text x="566" y="335">2</text>
      <circle cx="823" cy="390" r="14" fill="#fff" stroke="#ccc"/><text x="823" y="396">3</text>
      <circle cx="804" cy="641" r="14" fill="#fff" stroke="#ccc"/><text x="804" y="647">4</text>
      <circle cx="537" cy="709" r="14" fill="#fff" stroke="#ccc"/><text x="537" y="715">5</text>
    </g>
    <g class="step-arrows" fill="none" stroke="var(--arrow)" stroke-width="1.4" marker-end="url(#arrow-head)">
      <path d="M368 450 Q372 425 401 414"/>
      <path d="M680 357 Q705 350 725 367"/>
      <path d="M902 577 Q910 600 893 620"/>
      <path d="M711 808 Q692 828 667 826"/>
    </g>
  </svg>

  <div class="step-label" style="left:327px; top:542px; width:160px;">Attach Velcro<br>Pieces on Quilt</div>
  <div class="step-label" style="left:463px; top:350px; width:200px;">Insert Quilt into Cover</div>
  <div class="step-label" style="left:717px; top:421px; width:120px;">Fasten Quilt</div>
  <div class="step-label" style="left:721px; top:659px; width:160px;">Secure All Sides</div>
  <div class="step-label" style="left:440px; top:738px; width:100px;">Enjoy!</div>

  <h2 class="how-title">How it work?</h2>

  <div class="divider"></div>

  <section class="pitch">
    <h3 class="pitch-question">Frustrated every time you change the cover?&nbsp; Ever wish your quilt would just stay in place once it's in the cover?</h3>
    <h3 class="pitch-answer">We have the solution for you!</h3>
    <p class="pitch-body">The Quollin Snug-Fit Wrap is an innovative quilt cover that takes the chore we all hate - changing our covers - and makes it painless.&nbsp; The Snug-Fit Wrap opens on 3 sides, and lets you dress your quilt in 60 seconds.&nbsp; It also keeps your quilt in place at all times with strategically placed velcro pieces.&nbsp; Gone are the nights where you're left with a ball of cotton at the bottom and just a thin cover at the top, and you lie sideways in a fetal position trying to get as much warmth as possible.</p>
    <p class="pitch-body">And if that's not enough, our obsession for the highest quality fabric ensures you'll always enjoy a good night's rest.</p>
  </section>

  <footer class="footer">Copyright © 2011 to Quollin.</footer>
</body>
</html>
```